Fresh and Modern Real Estate Land Website

This Real Estate Agent sells only land.
The wordpress design will need to work well with responsive Avada theme.
Colors should complement the attached Home-Header.jpg, the Sonoran Desert, Southwest Region of Arizona and Tucson.
Home page layout to include
- Logo Attached: NewLogo.png
- Agent Photo: AdaMorton.jpg
- Contact Detials: use Phone
- Slogan: "I've Never Shown a House"
- Static header or Main image (see Attached Home-Header.jpg) - The dimensions of this shot may not be correct for your design. Please select from similar stock if needed and provide stock photo id.
- Intro/Welcome Text See Attached: Intro.txt
- Vertical or Horizontal display of "New" listings (include: Photo, Price, exerpt/intro) see: Properties.zip
- Tools of the trade. Home page will have a section called "Tools Of the Trade" These are items the agent uses in her work. This seciton will need to be 3 or More Images about 100 characters of text and Title. These will rotate through about 12 different tools. see: tools-of-the-trade.zip
Footer to include Contact Info/Recent Blog Posts/Testimonial
No Social Network icons
Main Menu:
Home
Properties
Testimonials
Services
About Ada
Blog
Contact
Real Estate
- Marck Script google/Times new Roman is logo. Designers Choice.

```html
<!DOCTYPE html>
<html lang="en">
<head>
<meta charset="utf-8">
<title>Ada Morton – Tucson's #1 Land Lady</title>
<link href="https://fonts.googleapis.com/css2?family=Open+Sans:wght@400;600;700&family=Marck+Script&display=swap" rel="stylesheet">
<style>
:root{
  --brown:#7b4e0f;
  --brown-dark:#5e3a08;
  --gold:#b7852c;
  --gold-light:#e0a53a;
  --ink:#222;
  --muted:#444;
  --line:#d9cbb8;
  --white:#fff;
}
*{box-sizing:border-box;margin:0;padding:0}
html,body{width:840px;height:1200px;overflow:hidden}
body{position:relative;background:var(--white);font-family:"Open Sans",Arial,sans-serif;color:var(--ink)}
.abs{position:absolute}

.site-header{left:0;top:0;width:840px;height:58px;background:var(--white)}
.brand{left:128px;top:12px}
.brand-name{font-size:21px;font-weight:700;color:var(--gold);line-height:1}
.brand-tag{font-size:6.5px;font-weight:700;color:var(--ink);letter-spacing:.2px;margin-top:2px}
.slogan{left:272px;top:29px;font-family:"Marck Script",cursive;font-size:13px;color:#444}
.call{left:594px;top:24px;display:flex;align-items:center;gap:4px}
.call-label{font-size:6.5px;font-weight:700;color:var(--gold);line-height:1}
.call-number{font-size:15px;font-weight:700;color:var(--gold);line-height:1.05}

.main-nav{left:0;top:58px;width:840px;height:26px;background:var(--brown);display:flex;align-items:center;padding-left:128px;gap:0}
.main-nav a{font-size:7px;font-weight:700;color:var(--white);text-decoration:none;margin-right:27px}
.main-nav a.active{color:var(--gold-light)}

.hero{left:0;top:84px;width:840px;height:280px;background:linear-gradient(180deg,#7f9fcf 0%,#c9d7ea 38%,#a89a6c 60%,#9a8450 80%,#7f6a3e 100%)}

.intro{left:0;top:364px;width:840px;height:157px;background:var(--gold);border-top:3px solid var(--brown);border-bottom:3px solid var(--brown)}
.agent-photo{left:128px;top:391px;width:70px;height:95px;border:2px solid var(--white);background:linear-gradient(180deg,#c9a58a,#d44a3a)}
.intro-title{left:207px;top:386px;font-size:18px;font-weight:700;color:var(--brown-dark)}
.intro-sub{left:207px;top:410px;font-size:14px;font-weight:700;color:var(--brown-dark)}
.intro-text{left:207px;top:433px;width:505px;font-size:8.8px;line-height:12px;color:var(--white)}
.chevron{left:400px;top:520px}

.section-title{left:0;width:840px;text-align:center;font-size:18px;font-weight:700;color:var(--ink)}
.tool{width:172px}
.tool-img{width:172px;height:133px;border:1px solid #bbb}
.tool h3{font-size:11.5px;font-weight:700;text-align:center;margin-top:6px}
.tool p{font-size:7.3px;line-height:12px;text-align:center;color:var(--muted);margin-top:1px;padding:0 16px}
.arrow{top:670px}

.listing{width:141px;height:144px;border:1px solid var(--line);background:var(--white)}
.listing h3{font-size:11.5px;font-weight:700;text-align:center;margin-top:7px}
.listing-img{position:relative;margin:3px 4px 0;width:131px;height:88px}
.listing-price{position:absolute;left:0;bottom:0;width:100%;height:18px;background:rgba(0,0,0,.75);color:var(--white);font-size:11px;font-weight:700;padding:2px 4px}
.listing p{font-size:7.2px;line-height:9px;text-align:center;color:var(--muted);margin-top:5px;padding:0 6px}

.site-footer{left:0;top:1009px;width:840px;height:191px;background:var(--brown)}
.foot-col h4{font-size:9px;font-weight:600;color:var(--white)}
.foot-col p,.foot-col li{font-family:Arial,sans-serif;font-size:6.8px;line-height:12px;color:var(--white);list-style:none}
.foot-link{font-size:8.5px;color:var(--gold-light)}
.badge{width:26px;height:26px;border:2px solid var(--white)}
.foot-rule{left:0;top:1164px;width:840px;height:1px;background:#94672a}
.copyright{left:0;top:1174px;width:840px;text-align:center;font-family:Arial,sans-serif;font-size:6.8px;color:var(--white)}
.copyright span{color:var(--gold-light)}
</style>
</head>
<body>

<header class="site-header abs">
  <div class="brand abs">
    <div class="brand-name">Ada Morton</div>
    <div class="brand-tag">TUCSON'S #1 LAND LADY</div>
  </div>
  <div class="slogan abs">I've Never Shown a House</div>
  <div class="call abs">
    <svg width="20" height="20" viewBox="0 0 20 20"><circle cx="10" cy="10" r="9" fill="none" stroke="#7b4e0f" stroke-width="1.6"/><path d="M7 5.5c-1 .6-1.4 1.8-.8 3.4.9 2.4 2.5 4 4.9 4.9 1.6.6 2.8.2 3.4-.8l-1.8-1.6-1.3.8c-1-.5-2.2-1.7-2.7-2.7l.8-1.3z" fill="#7b4e0f"/></svg>
    <div><div class="call-label">CALL ON US</div><div class="call-number">000 000 0000</div></div>
  </div>
</header>

<nav class="main-nav abs">
  <a class="active" href="#">HOME</a><a href="#">ADA'S LISTINGS</a><a href="#">SERVICES</a><a href="#">ABOUT ADA</a><a href="#">TESTIMONIALS</a><a href="#">BLOG</a><a href="#">CONTACT</a>
</nav>

<div class="hero abs" role="img" aria-label="Sonoran desert highway with a tall saguaro cactus under a cloudy blue sky"></div>

<section class="intro abs"></section>
<div class="agent-photo abs" role="img" aria-label="Portrait of agent Ada Morton"></div>
<h1 class="intro-title abs">Ada Morton - The Land Lady!</h1>
<h2 class="intro-sub abs">Tucosn's Leading Land Realtor</h2>
<p class="intro-text abs">When you are looking for Tucson land, Ada Morton's 30+ years of experience has "landed" her among the top 1/2% of Realtors in the United States... just selling dirt! With nearly $200 million in sales, Ada has vast experience in negotiations and the physical aspects of land - slopes, soil conditions, site work, hydrology, latest zoning changes, future development and other factors that go into purchasing land. Ada believes it's her job to invest her time in answering your questions so that you don't have to waste yours. She truly DIGS DIRT!</p>
<svg class="chevron abs" width="40" height="20" viewBox="0 0 40 20"><path d="M0 0h40L20 20z" fill="#7b4e0f"/><path d="M15 6l5 5 5-5" fill="none" stroke="#fff" stroke-width="2"/></svg>

<h2 class="section-title abs" style="top:557px">TOOLS OF MY TRADE... no LockBox Here!</h2>
<svg class="arrow abs" style="left:109px" width="20" height="38" viewBox="0 0 20 38"><path d="M20 0v38L0 19z" fill="#222"/><path d="M13 14l-5 5 5 5" fill="none" stroke="#e0a53a" stroke-width="2"/></svg>
<div class="tool abs" style="left:143px;top:601px">
  <div class="tool-img" role="img" aria-label="Yellow surveyor's tape measure" style="background:radial-gradient(circle,#e8c640 0%,#f4f0e0 65%,#fff 100%)"></div>
  <h3>TAPE-MEASURE</h3><p>Lorem Ipsum is simply dummy text of the printing and typesetting industry.</p>
</div>
<div class="tool abs" style="left:334px;top:601px">
  <div class="tool-img" role="img" aria-label="Field compass beside its leather case" style="background:radial-gradient(circle,#5a4030 0%,#d8d4cc 65%,#fff 100%)"></div>
  <h3>COMPAS</h3><p>Lorem Ipsum is simply dummy text of the printing and typesetting industry.</p>
</div>
<div class="tool abs" style="left:525px;top:601px">
  <div class="tool-img" role="img" aria-label="Roll of orange flagging tape" style="background:radial-gradient(circle,#ff5a20 0%,#ffd8c8 60%,#fff 100%)"></div>
  <h3>ORANGE TAPE</h3><p>Lorem Ipsum is simply dummy text of the printing and typesetting industry.</p>
</div>
<svg class="arrow abs" style="left:713px" width="20" height="38" viewBox="0 0 20 38"><path d="M0 0v38L20 19z" fill="#222"/><path d="M7 14l5 5-5 5" fill="none" stroke="#fff" stroke-width="2"/></svg>

<h2 class="section-title abs" style="top:800px">ADA'S LISTINGS</h2>
<div class="listing abs" style="left:128px;top:839px">
  <h3>NORTH</h3>
  <div class="listing-img" role="img" aria-label="Desert sunset over north Tucson land" style="background:linear-gradient(180deg,#e8a020,#c06010 60%,#2a1a08)"><div class="listing-price">$200</div></div>
  <p>Lorem Ipsum is simply dummy text of the.</p>
</div>
<div class="listing abs" style="left:275px;top:839px">
  <h3>NORTHWEST</h3>
  <div class="listing-img" role="img" aria-label="Green desert scrub below mountains" style="background:linear-gradient(180deg,#a8c0dc,#9aa0a0 35%,#5e7040 60%,#4a5a30)"><div class="listing-price">$200</div></div>
  <p>Lorem Ipsum is simply dummy text of the.</p>
</div>
<div class="listing abs" style="left:423px;top:839px">
  <h3>NORTHEAST</h3>
  <div class="listing-img" role="img" aria-label="Saguaro cacti on desert land with mountains" style="background:linear-gradient(180deg,#6a9ad8,#b0b8c0 35%,#6a7040 60%,#4a4a28)"><div class="listing-price">$200</div></div>
  <p>Lorem Ipsum is simply dummy text of the.</p>
</div>
<div class="listing abs" style="left:571px;top:839px">
  <h3>ALL AREAS</h3>
  <div class="listing-img" role="img" aria-label="Orange rock formations" style="background:linear-gradient(160deg,#c05020,#f08040 45%,#a03818)"><div class="listing-price">$200</div></div>
  <p>Lorem Ipsum is simply dummy text of the.</p>
</div>

<footer class="site-footer abs"></footer>
<div class="foot-col abs" style="left:128px;top:1030px;width:180px">
  <h4>Contact Info</h4>
  <p style="margin-top:6px"><svg width="8" height="8" viewBox="0 0 8 8"><path d="M4 0L0 4h1v4h2V5h2v3h2V4h1z" fill="#e0a53a"/></svg> Lorem Ipsum is simply dummy text of the printing and typesetting industry.</p>
  <p style="margin-top:4px"><svg width="11" height="8" viewBox="0 0 11 8"><path d="M0 3c2-3 9-3 11 0l-2 1-1-1H3L2 4zM2 5h7v3H2z" fill="#e0a53a"/></svg> (+00) 000 12345 &nbsp;&nbsp; <svg width="10" height="7" viewBox="0 0 10 7"><rect width="10" height="7" fill="#e0a53a"/><path d="M0 0l5 4 5-4" fill="none" stroke="#7b4e0f"/></svg> mail@example.com</p>
  <div style="display:flex;gap:12px;margin-top:26px"><div class="badge"></div><div class="badge" style="width:44px"></div></div>
</div>
<div class="foot-col abs" style="left:371px;top:1030px">
  <h4>Recent Blog Posts</h4>
  <ul style="margin-top:6px;line-height:15px">
    <li style="line-height:15px">Blog Slideshow Post</li><li style="line-height:15px">Aenean Odio Mauris</li><li style="line-height:15px">Blog Image Post</li><li style="line-height:15px">Blog Video Post</li><li style="line-height:15px">Donec Suscipit Dim Euismods</li>
  </ul>
  <div class="foot-link" style="margin-top:14px">See All Blog Posts</div>
</div>
<div class="foot-col abs" style="left:535px;top:1030px;width:170px">
  <h4>Testimonial</h4>
  <p style="margin-top:6px">Ada is proud to say that she STILL has never sold a house... but she does know the best who do. 90% of real estate is sold by 10% of the Realtors and, during nearly 30 years of selling, Ada knows and is good friends with these 10%. Utilize Ada's contacts so she can match up the right home agent...for YOU!</p>
  <div class="foot-link" style="margin-top:6px">See All Testimonials</div>
</div>
<div class="foot-rule abs"></div>
<div class="copyright abs">© 2014 <span>Ada Morton</span>, All Rights Reserved</div>

</body>
</html>
```